Rebrand existing website with new identity and colours as supplied

I have an old website that I would like updating with a new identity.
The website is at www.larchvalefunding.com
The new branding and changes are as set out below.

Target Market(s)

Buyers and sellers of SME businesses

Industry/Entity Type

Financial services

Coding

Coded - Design and coding required

Number of Pages Required

4 page

Requirements
Must have
• In addition to the small number of new pages I would like to retain the existing structure and pages - simply rebranded

```html
<!DOCTYPE html>
<html lang="en">
<head>
<meta charset="utf-8">
<title>Larchvale Funding – Help to buy a business</title>
<link rel="stylesheet" href="https://fonts.googleapis.com/css2?family=Cabin:wght@600;700&family=Heebo:wght@400;500;700&family=Montserrat:wght@900&display=swap">
<style>
:root{
  --navy:#141b45;
  --navy-deep:#111738;
  --card:#151c42;
  --red:#ee1b24;
  --ink:#1d2040;
  --body:#555a66;
  --line:#cfd2d8;
  --ghost:#e9eaee;
  --white:#ffffff;
}
*{box-sizing:border-box;margin:0;padding:0}
html,body{width:1200px;height:3542px;overflow:hidden}
body{position:relative;background:var(--white);font-family:'Heebo',sans-serif;color:var(--ink)}
.abs{position:absolute}
.heading{font-family:'Cabin',sans-serif;font-weight:700}
.accent{color:var(--red)}
svg{display:block}

/* header */
.brand{left:110px;top:30px;display:flex;align-items:center;gap:10px}
.brand-mark{width:22px;height:22px;background:var(--red)}
.brand-name{font-family:'Cabin',sans-serif;font-weight:700;font-size:30px;color:var(--navy);letter-spacing:-.3px}
.nav{left:440px;top:44px;display:flex;gap:0;font-size:15px;font-weight:500;color:var(--ink)}
.nav a{color:inherit;text-decoration:none;position:absolute;white-space:nowrap}
.nav a.active{color:var(--red)}
.nav a.active::after{content:"";position:absolute;left:50%;bottom:-9px;width:22px;height:2px;margin-left:-11px;background:var(--red)}

/* hero */
.hero-text{left:113px;top:270px;width:470px}
.hero-title{font-size:45px;line-height:46px;color:var(--navy)}
.hero-lead{margin-top:22px;font-size:15.5px;line-height:26px;color:#2b2d36;font-weight:500}
.btn{display:inline-flex;align-items:center;justify-content:center;gap:8px;background:var(--red);color:var(--white);font-weight:700;font-size:15.5px;border-radius:30px;text-transform:uppercase}
.btn-dot{width:14px;height:14px;border-radius:50%;background:var(--white);display:inline-block;position:relative}
.btn-dot::after{content:"";position:absolute;left:4px;top:4px;border-left:6px solid var(--red);border-top:3px solid transparent;border-bottom:3px solid transparent}
.round-btn{border-radius:50%;background:var(--white);box-shadow:0 4px 14px rgba(20,27,69,.25);display:flex;align-items:center;justify-content:center}

/* vertical labels */
.side-label{font-family:'Montserrat',sans-serif;font-weight:900;writing-mode:vertical-rl;white-space:nowrap}
.side-up{transform:rotate(180deg)}

/* about */
.section-kicker{font-size:15px;font-weight:700;color:var(--red);display:flex;align-items:center;gap:10px}
.section-kicker::before{content:"";width:20px;height:3px;background:var(--red)}
.about-title{font-size:40px;color:var(--navy);margin-top:8px}
.about-copy p{font-size:14.5px;line-height:26px;color:var(--body);text-align:justify;margin-bottom:13px}

/* services */
.services-title{left:0;width:1200px;top:1543px;text-align:center;font-size:41px;color:var(--white)}
.card{background:var(--card);width:312px;height:240px;text-align:center;color:var(--white)}
.card-icon{margin:22px auto 0;width:62px;height:62px}
.card h3{font-size:19px;font-weight:700;margin-top:12px}
.card p{font-size:14.5px;line-height:24px;color:#d9dbe6;margin:12px 24px 0}
.card-toggle{position:absolute;left:50%;bottom:-18px;margin-left:-18px;width:36px;height:36px;border-radius:50%;background:var(--red);box-shadow:0 3px 8px rgba(0,0,0,.35);display:flex;align-items:center;justify-content:center}

/* contact */
.contact-title{left:0;width:1200px;top:2400px;text-align:center;font-size:41px;color:var(--navy)}
.form-card{left:462px;top:2545px;width:624px;height:434px;background:var(--white);box-shadow:0 10px 40px rgba(20,27,69,.12)}
.form-card h3{position:absolute;left:52px;top:40px;font-size:26px;color:var(--navy)}
.field{position:absolute;width:229px}
.field label{display:block;font-size:14.5px;font-weight:500;color:var(--ink)}
.field span{display:block;margin-top:12px;padding-bottom:10px;font-size:12.5px;color:#7a7d88;border-bottom:1px solid var(--line)}

/* footer */
.foot-col h4{font-size:17px;font-weight:700;color:var(--white)}
.foot-col ul{list-style:none;margin-top:18px}
.foot-col li{font-size:14px;color:#d5d8e4;line-height:25.6px}
.subscribe{left:810px;top:3323px;width:277px;height:44px;border-radius:24px;background:var(--white);overflow:hidden}
.subscribe span{position:absolute;left:22px;top:14px;font-size:12.5px;color:#7a7d88}
.subscribe b{position:absolute;right:0;top:0;width:122px;height:44px;background:var(--red);border-radius:24px;color:var(--white);font-size:17px;display:flex;align-items:center;justify-content:center}
.copyright{left:0;top:3498px;width:1200px;text-align:center;font-size:15px;color:#e1e3ec}
</style>
</head>
<body>

<!-- hero backdrop -->
<svg class="abs" style="left:0;top:0" width="1200" height="860" viewBox="0 0 1200 860">
  <defs>
    <linearGradient id="heroTone" x1="0" y1="0" x2="1" y2="1">
      <stop offset="0" stop-color="#eef0f2"/>
      <stop offset=".55" stop-color="#d9dcdf"/>
      <stop offset="1" stop-color="#b9bec6"/>
    </linearGradient>
  </defs>
  <polygon points="0,0 1200,0 1200,672 0,777" fill="url(#heroTone)" role="img" aria-label="Overhead photo of a business team meeting around a white sofa with charts and coffee"/>
  <polygon points="632,718 1200,672 1200,842" fill="var(--red)"/>
</svg>

<!-- header -->
<div class="abs brand">
  <span class="brand-mark"></span>
  <span class="brand-name">Larchvale Funding Ltd</span>
</div>
<nav class="abs nav" style="left:0;top:45px">
  <a class="active" href="#" style="left:457px">Home</a>
  <a href="#" style="left:533px">About</a>
  <a href="#" style="left:609px">Working Capital</a>
  <a href="#" style="left:753px">Property Finance</a>
  <a href="#" style="left:905px">How we work</a>
  <a href="#" style="left:1032px">Contact</a>
</nav>

<!-- hero copy -->
<div class="abs hero-text">
  <h1 class="heading hero-title">All the help you need<br>to <span class="accent">buy a business</span></h1>
  <p class="hero-lead">It isn't every day that you purchase a business, and we appreciate<br>that it can be a difficult time for both buyer and seller</p>
</div>
<a class="abs btn" href="#" style="left:114px;top:463px;width:205px;height:50px;text-decoration:none">Get Started <span class="btn-dot"></span></a>

<div class="abs round-btn" style="left:570px;top:694px;width:60px;height:60px">
  <svg width="22" height="22" viewBox="0 0 22 22" fill="none" stroke="var(--navy)" stroke-width="2.2" stroke-linecap="round" stroke-linejoin="round"><path d="M5 5l6 6 6-6M5 11l6 6 6-6"/></svg>
</div>

<!-- about -->
<div class="abs side-label side-up" style="left:30px;top:912px;font-size:58px;color:var(--ghost);line-height:58px">ABOUT US</div>
<div class="abs" style="left:86px;top:1011px;width:338px;height:311px;border:3px solid var(--navy)"></div>
<div class="abs" style="left:111px;top:865px;width:422px;height:431px;background:linear-gradient(135deg,#5b4638 0%,#9a8c82 45%,#d8d6d6 100%)" role="img" aria-label="Photo of three colleagues reviewing documents at a laptop"></div>

<div class="abs" style="left:603px;top:868px;width:485px">
  <div class="section-kicker">ABOUT US</div>
  <h2 class="heading about-title">Larchvale Funding</h2>
  <div class="about-copy" style="margin-top:16px">
    <p>It isn't every day that you purchase a business, and we appreciate that it can be a difficult time for both buyer and seller, often requiring a range of skills not needed at any other time in a business lifetime.</p>
    <p>Even after a price is agreed, agreeing the best split between up-front and deferred consideration can be vital in the success of a purchase both at completion and in the years ahead.</p>
    <p>Although there are many potential funders the right acquisition debt package can still be hard to find and complex to negotiate.That is where Larchvale Funding can help, we have the tools, the experience, and the contacts to help you evaluate, structure, and fund your acquisition.</p>
  </div>
</div>
<a class="abs btn" href="#" style="left:603px;top:1268px;width:187px;height:42px;font-size:15px;text-decoration:none">Contact Us <span class="btn-dot"></span></a>

<!-- services band -->
<svg class="abs" style="left:0;top:1370px" width="1200" height="990" viewBox="0 1370 1200 990">
  <defs>
    <linearGradient id="bandTone" x1="0" y1="0" x2="0" y2="1">
      <stop offset="0" stop-color="#1c2457"/>
      <stop offset=".5" stop-color="#192150"/>
      <stop offset="1" stop-color="#141b45"/>
    </linearGradient>
  </defs>
  <polygon points="0,1375 474,1482 0,1526" fill="var(--red)"/>
  <polygon points="0,1526 1200,1416 1200,2238 0,2348" fill="url(#bandTone)" role="img" aria-label="Faded city skyline with financial chart overlay in navy"/>
</svg>

<h2 class="abs heading services-title">Working Capital <span class="accent">Finance</span></h2>
<div class="abs side-label" style="left:1120px;top:1660px;font-size:58px;line-height:58px;color:rgba(255,255,255,.1)">OUR SERVICES</div>

<!-- row 1 -->
<div class="abs card" style="left:111px;top:1630px">
  <svg class="card-icon" viewBox="0 0 62 62" fill="none" stroke="#fff" stroke-width="2" stroke-linejoin="round"><path d="M8 56h46M14 56V22h14v34M28 56V10h14v46M42 56V30h8v26"/><path d="M18 28h6M18 36h6M18 44h6M32 16h6M32 24h6M32 32h6M32 40h6"/><circle cx="48" cy="44" r="8"/></svg>
  <h3>Business Loans</h3>
  <p>Types of business loans are of many types but fall in to two broad categories, secured and unsecured.</p>
  <span class="card-toggle"><svg width="14" height="14" viewBox="0 0 14 14" fill="none" stroke="#fff" stroke-width="2.4" stroke-linecap="round" stroke-linejoin="round"><path d="M3 5l4 4 4-4"/></svg></span>
</div>
<div class="abs card" style="left:444px;top:1630px">
  <svg class="card-icon" viewBox="0 0 62 62" fill="none" stroke="#fff" stroke-width="2" stroke-linejoin="round"><rect x="20" y="6" width="30" height="40"/><rect x="12" y="16" width="30" height="40"/><path d="M18 26h18M18 34h18M18 42h12"/><circle cx="40" cy="18" r="5"/></svg>
  <h3>Invoice Finance</h3>
  <p>Although only available in recent years, for a few years, Business cash advances are increasingly popular</p>
  <span class="card-toggle"><svg width="14" height="14" viewBox="0 0 14 14" fill="none" stroke="#fff" stroke-width="2.4" stroke-linecap="round" stroke-linejoin="round"><path d="M3 5l4 4 4-4"/></svg></span>
</div>
<div class="abs card" style="left:777px;top:1630px">
  <svg class="card-icon" viewBox="0 0 62 62" fill="none" stroke="#fff" stroke-width="2" stroke-linejoin="round"><rect x="22" y="12" width="32" height="20" rx="2"/><path d="M22 19h32"/><circle cx="50" cy="10" r="6"/><path d="M6 52l12-12h14l8 6-10 4H20"/><path d="M6 58l14-2 22-10"/></svg>
  <h3>Revolving Credit Facilities</h3>
  <p>Like a bank overdraft, revolving credit facilities provide a useful source of pre-approved, short-term,</p>
  <span class="card-toggle"><svg width="14" height="14" viewBox="0 0 14 14" fill="none" stroke="#fff" stroke-width="2.4" stroke-linecap="round" stroke-linejoin="round"><path d="M3 5l4 4 4-4"/></svg></span>
</div>

<!-- row 2 -->
<div class="abs card" style="left:111px;top:1914px">
  <svg class="card-icon" viewBox="0 0 62 62" fill="none" stroke="#fff" stroke-width="2" stroke-linejoin="round"><path d="M12 6h30l8 8v36H12z"/><rect x="18" y="12" width="22" height="10"/><path d="M18 30h24M18 36h24M18 42h16"/><circle cx="46" cy="48" r="9"/><path d="M42 48l3 3 6-6"/></svg>
  <h3>Tax bill and VAT funding</h3>
  <p>Fortunately, in recent years a number of specialist lenders have introduced facilities specifically</p>
  <span class="card-toggle"><svg width="14" height="14" viewBox="0 0 14 14" fill="none" stroke="#fff" stroke-width="2.4" stroke-linecap="round" stroke-linejoin="round"><path d="M3 5l4 4 4-4"/></svg></span>
</div>
<div class="abs card" style="left:444px;top:1914px">
  <svg class="card-icon" viewBox="0 0 62 62" fill="none" stroke="#fff" stroke-width="2" stroke-linejoin="round"><rect x="6" y="8" width="50" height="34"/><path d="M14 36V26M22 36V18M30 36V22M38 36V14"/><path d="M12 22l10-8 8 4 14-10"/><path d="M4 48h54M20 48v8h22v-8"/><rect x="44" y="26" width="12" height="14"/></svg>
  <h3>Trade Finance</h3>
  <p>As a distributor, or importer, you may be looking for ways to close the payment gap at the start of your sales cycle.</p>
  <span class="card-toggle"><svg width="14" height="14" viewBox="0 0 14 14" fill="none" stroke="#fff" stroke-width="2.4" stroke-linecap="round" stroke-linejoin="round"><path d="M3 5l4 4 4-4"/></svg></span>
</div>
<div class="abs card" style="left:777px;top:1914px">
  <svg class="card-icon" viewBox="0 0 62 62" fill="none" stroke="#fff" stroke-width="2" stroke-linejoin="round"><rect x="10" y="4" width="42" height="54"/><rect x="14" y="8" width="34" height="10"/><path d="M16 26h30M16 32h18M16 38h18M16 44h18M16 50h30"/><rect x="36" y="30" width="12" height="14"/></svg>
  <h3>Invoice Finance</h3>
  <p>Types of business loans are of many types but fall in to two broad categories, secured and unsecured.</p>
  <span class="card-toggle"><svg width="14" height="14" viewBox="0 0 14 14" fill="none" stroke="#fff" stroke-width="2.4" stroke-linecap="round" stroke-linejoin="round"><path d="M3 5l4 4 4-4"/></svg></span>
</div>

<!-- contact -->
<h2 class="abs heading contact-title">Contact <span class="accent">Us</span></h2>
<div class="abs side-label side-up" style="left:26px;top:2466px;font-size:58px;line-height:58px;color:var(--ghost)">GET IN TOUCH</div>

<div class="abs" style="left:109px;top:2492px;width:446px;height:385px;background:linear-gradient(135deg,#ee1b24 0%,#e3161f 55%,#c9111a 100%)" role="img" aria-label="Red-toned photo of a smiling businessman holding a tablet"></div>
<div class="abs heading" style="left:160px;top:2618px;width:240px;text-align:right;font-size:38px;line-height:43px;color:var(--white)">Let's Do<br>Good<br>Together!</div>

<div class="abs" style="left:742px;top:2513px;width:366px;height:347px;border:3px solid var(--navy)"></div>

<div class="abs form-card">
  <h3 class="heading">Send Us A Message</h3>
  <div class="field" style="left:56px;top:106px"><label>Your Name</label><span>Alex Reed</span></div>
  <div class="field" style="left:333px;top:106px"><label>Company</label><span>Lorem ipsum dolor sit amet</span></div>
  <div class="field" style="left:56px;top:198px"><label>Email Address</label><span>alex.reed@larchvalefunding.com</span></div>
  <div class="field" style="left:333px;top:198px"><label>Phone</label><span>01632-960-482</span></div>
  <div class="field" style="left:56px;top:292px;width:444px"><label>Message</label><span style="padding-bottom:40px">Hi, do you have a moment to talk abo...|</span></div>
  <div class="abs" style="left:501px;top:324px;width:64px;height:64px;border-radius:50%;background:var(--red);box-shadow:0 6px 16px rgba(238,27,36,.35);display:flex;align-items:center;justify-content:center">
    <svg width="24" height="24" viewBox="0 0 24 24" fill="#fff"><path d="M22 2L2 11l7 3 2 8 3-6 5 4z"/><path d="M9 14l13-12-10 14z" fill="#f7c3c5"/></svg>
  </div>
</div>

<!-- footer -->
<svg class="abs" style="left:0;top:3030px" width="1200" height="512" viewBox="0 3030 1200 512">
  <polygon points="0,3100 632,3169 1200,3210 1200,3542 0,3542" fill="var(--navy)"/>
  <polygon points="632,3169 1200,3038 1200,3210" fill="var(--red)"/>
</svg>
<div class="abs round-btn" style="left:568px;top:3123px;width:64px;height:64px;border:4px solid var(--white);background:var(--white);box-shadow:0 0 0 2px var(--navy)">
  <svg width="22" height="22" viewBox="0 0 22 22" fill="none" stroke="var(--navy)" stroke-width="2.2" stroke-linecap="round" stroke-linejoin="round"><path d="M5 11l6-6 6 6M5 17l6-6 6 6"/></svg>
</div>

<div class="abs brand" style="left:110px;top:3318px">
  <span class="brand-mark"></span>
  <span class="brand-name" style="color:var(--white);font-size:30px">Larchvale Funding Ltd</span>
</div>
<span class="abs" style="left:177px;top:3402px;width:30px;height:30px;border-radius:50%;background:var(--red)"></span>
<span class="abs" style="left:216px;top:3402px;width:30px;height:30px;border-radius:50%;background:var(--white)"></span>

<div class="abs foot-col" style="left:433px;top:3274px">
  <h4>Quick Links</h4>
  <ul><li>Home</li><li>About</li><li>Working Capital</li><li>Property Finance</li><li>How we work</li></ul>
</div>
<div class="abs foot-col" style="left:611px;top:3274px">
  <h4>About Company</h4>
  <ul><li>Terms of Use</li><li>Terms &amp; Condition</li><li>Privacy Policy</li><li>Contact</li></ul>
</div>
<div class="abs foot-col" style="left:804px;top:3274px">
  <h4 style="font-size:18.5px">Subscribe for Updates</h4>
</div>
<div class="abs subscribe"><span>Emaill Address</span><b>SUBMIT</b></div>
<div class="abs" style="left:804px;top:3392px;display:flex;align-items:center;gap:10px;font-size:14px;font-weight:500;color:var(--white)">
  <svg width="14" height="14" viewBox="0 0 14 14" fill="none" stroke="#fff" stroke-width="1.5"><rect x="1" y="2" width="11" height="11" rx="2"/><path d="M4 7l2.5 2.5L13 2"/></svg>
  Yes, Please Contact me.
</div>

<div class="abs" style="left:1131px;top:3438px;width:36px;height:36px;border-radius:50%;background:var(--red);display:flex;align-items:center;justify-content:center">
  <svg width="14" height="14" viewBox="0 0 14 14" fill="none" stroke="#fff" stroke-width="2.4" stroke-linecap="round" stroke-linejoin="round"><path d="M3 9l4-4 4 4"/></svg>
</div>

<p class="abs copyright">2022 Copyright - Larchvale Funding. | All Rights Reserved</p>

</body>
</html>
```